International Consulting Firm
Stationery incl. business cards, letterhead, envelope, PPT template, and brochure
Professional
DMN QRT
CHIEF EXECUTIVE OFFICER
LEVEL 4,
7 MOOR LANE
FERN HOUSE
GOTHAM CITY
DMN@DORSETTPRYCE.EXAMPLE
WWW.DORSETTPRYCE.EXAMPLE
The fonts used in the logo are (a) Eras Bold ITC & (b)BankGothic
Logo only
This fantastic logo was designed recently by quarbin and we now need stationery to support it.

```html
<!DOCTYPE html>
<html lang="en">
<head>
<meta charset="utf-8">
<title>Dorsett Pryce Stationery</title>
<link rel="stylesheet" href="https://fonts.googleapis.com/css2?family=Michroma&family=Montserrat:wght@400;600;700&display=swap">
<style>
  :root {
    --bronze-dark: #5a3418;
    --bronze-mid: #a8723f;
    --bronze-light: #d8ab78;
    --ink: #111111;
    --paper: #ffffff;
    --rule: #9a9a9a;
    --faint: #ececec;
    --muted: #555555;
  }
  * { box-sizing: border-box; margin: 0; padding: 0; }
  html, body { width: 1200px; height: 502px; overflow: hidden; }
  body { font-family: "Montserrat", sans-serif; color: var(--ink); }
  .canvas {
    position: relative; width: 1200px; height: 502px; overflow: hidden;
    background: radial-gradient(ellipse at 45% 40%, var(--bronze-light) 0%, var(--bronze-mid) 45%, var(--bronze-dark) 100%);
  }
  .sheet { position: absolute; background: var(--paper); overflow: hidden; box-shadow: 0 2px 6px rgba(0,0,0,.35); }
  .sheet svg.curve { position: absolute; left: 0; top: 0; }
  .brand { position: absolute; display: flex; align-items: center; gap: 5px; }
  .brand-dot { border-radius: 50%; }
  .brand-name { font-family: "Michroma", sans-serif; font-weight: 400; letter-spacing: .5px; white-space: nowrap; }
  .brand--light .brand-dot { background: var(--paper); }
  .brand--light .brand-name { color: var(--paper); }
  .brand--dark .brand-dot { background: var(--ink); }
  .brand--dark .brand-name { color: var(--ink); }
  .faint-mark { position: absolute; border-radius: 50%; background: var(--faint); }
  .footer-text { position: absolute; font-size: 6px; line-height: 1.45; color: var(--muted); text-align: center; }

  /* envelope */
  .envelope { left: 19px; top: 269px; width: 240px; height: 211px; }
  .envelope .return-address { left: 120px; bottom: 14px; text-align: left; }

  /* letterhead */
  .letterhead { left: 252px; top: 29px; width: 372px; height: 463px; }

  /* business cards */
  .card { width: 150px; }
  .card--front { left: 643px; top: 103px; height: 96px; }
  .card--black { left: 643px; top: 331px; height: 72px; background: var(--ink); }
  .card--plain { left: 643px; top: 432px; height: 48px; }
  .card-details { position: absolute; right: 8px; top: 30px; font-size: 4.6px; line-height: 1.45; text-align: right; color: var(--muted); }
  .card-details .person { font-weight: 700; color: var(--ink); font-size: 5.4px; }

  /* fax */
  .fax { left: 809px; top: 12px; width: 372px; height: 480px; }
  .fax-title { position: absolute; left: 22px; right: 22px; top: 78px; height: 18px; background: var(--ink); color: var(--paper); font-weight: 700; font-size: 11px; padding: 3px 8px; }
  .fax-table { position: absolute; left: 22px; right: 22px; top: 98px; border-collapse: collapse; font-size: 7px; }
  .fax-table td { border: 1px solid var(--rule); height: 17px; padding: 0 5px; }
  .fax-table td.label { width: 40px; font-weight: 600; }
  .fax-checks { position: absolute; left: 22px; right: 22px; top: 182px; display: flex; justify-content: space-between; font-size: 6.5px; }
  .fax-checks span::before { content: ""; display: inline-block; width: 7px; height: 7px; border: 1px solid var(--ink); margin-right: 4px; vertical-align: -1px; }
  .fax-comments { position: absolute; left: 22px; top: 204px; font-size: 7px; font-weight: 600; }
</style>
</head>
<body>
<main class="canvas">

  <!-- Envelope -->
  <section class="sheet envelope" aria-label="Envelope">
    <svg class="curve" width="240" height="211" viewBox="0 0 240 211">
      <path d="M0 0 H240 V62 C170 68 90 78 0 112 Z" fill="var(--ink)"/>
      <path d="M0 118 C90 84 170 72 240 68" fill="none" stroke="var(--rule)" stroke-width="1"/>
    </svg>
    <div class="faint-mark" style="left:150px;top:110px;width:70px;height:70px"></div>
    <div class="brand brand--light" style="left:14px;top:44px">
      <span class="brand-dot" style="width:14px;height:14px"></span>
      <span class="brand-name" style="font-size:7px">DORSETT PRYCE</span>
    </div>
    <p class="footer-text return-address">LEVEL 4, 7 MOOR LANE, FERN HOUSE<br>GOTHAM CITY 12345</p>
  </section>

  <!-- Letterhead -->
  <section class="sheet letterhead" aria-label="Letterhead">
    <svg class="curve" width="372" height="130" viewBox="0 0 372 130">
      <path d="M0 0 H372 V68 C270 60 140 70 0 118 Z" fill="var(--ink)"/>
      <path d="M0 126 C140 78 270 68 372 76" fill="none" stroke="var(--rule)" stroke-width="1"/>
    </svg>
    <div class="brand brand--light" style="left:20px;top:34px">
      <span class="brand-dot" style="width:18px;height:18px"></span>
      <span class="brand-name" style="font-size:8px">DORSETT PRYCE</span>
    </div>
    <div class="faint-mark" style="left:120px;top:190px;width:150px;height:150px"></div>
    <p class="footer-text" style="left:0;right:0;bottom:12px">
      LEVEL 4, 7 MOOR LANE, FERN HOUSE, GOTHAM CITY 12345<br>
      P: (02) 5550 1234 &nbsp;|&nbsp; F: (02) 5550 1235 &nbsp;|&nbsp; WWW.DORSETTPRYCE.EXAMPLE
    </p>
  </section>

  <!-- Business card: details -->
  <section class="sheet card card--front" aria-label="Business card front">
    <svg class="curve" width="150" height="96" viewBox="0 0 150 96">
      <path d="M0 0 H150 V12 C100 14 50 22 0 40 Z" fill="var(--ink)"/>
      <path d="M0 44 C50 26 100 18 150 16" fill="none" stroke="var(--rule)" stroke-width=".6"/>
    </svg>
    <div class="brand brand--light" style="left:6px;top:4px">
      <span class="brand-dot" style="width:9px;height:9px"></span>
      <span class="brand-name" style="font-size:4.5px">DORSETT PRYCE</span>
    </div>
    <div class="card-details">
      <p class="person">DMN QRT</p>
      <p>CHIEF EXECUTIVE OFFICER</p>
      <p>LEVEL 4, 7 MOOR LANE</p>
      <p>FERN HOUSE, GOTHAM CITY</p>
      <p>DMN@DORSETTPRYCE.EXAMPLE</p>
      <p>WWW.DORSETTPRYCE.EXAMPLE</p>
    </div>
  </section>

  <!-- Business card: black back -->
  <section class="sheet card card--black" aria-label="Business card back">
    <div class="brand brand--light" style="left:14px;top:28px">
      <span class="brand-dot" style="width:14px;height:14px"></span>
      <span class="brand-name" style="font-size:6px">DORSETT PRYCE</span>
    </div>
  </section>

  <!-- Business card: white back -->
  <section class="sheet card card--plain" aria-label="Business card alternate back">
    <div class="brand brand--dark" style="left:14px;top:17px">
      <span class="brand-dot" style="width:12px;height:12px"></span>
      <span class="brand-name" style="font-size:5.5px">DORSETT PRYCE</span>
    </div>
  </section>

  <!-- Fax cover -->
  <section class="sheet fax" aria-label="Fax cover sheet">
    <div class="brand brand--dark" style="left:22px;top:26px">
      <span class="brand-dot" style="width:22px;height:22px"></span>
      <span class="brand-name" style="font-size:8px">DORSETT PRYCE</span>
    </div>
    <div class="fax-title">FAX</div>
    <table class="fax-table">
      <tr><td class="label">To:</td><td></td><td class="label">Phone:</td><td></td></tr>
      <tr><td class="label">Fax:</td><td></td><td class="label">Pages:</td><td></td></tr>
      <tr><td class="label">Phone:</td><td></td><td class="label">Date:</td><td></td></tr>
      <tr><td class="label">Re:</td><td></td><td class="label">CC:</td><td></td></tr>
    </table>
    <div class="fax-checks">
      <span>Urgent</span><span>For Review</span><span>Please Comment</span><span>Please Reply</span><span>Please Recycle</span>
    </div>
    <p class="fax-comments">Comments:</p>
    <div class="faint-mark" style="left:120px;top:250px;width:140px;height:140px"></div>
    <p class="footer-text" style="left:0;right:0;bottom:12px">
      LEVEL 4, 7 MOOR LANE, FERN HOUSE, GOTHAM CITY 12345<br>
      P: (02) 5550 1234 &nbsp;|&nbsp; F: (02) 5550 1235 &nbsp;|&nbsp; WWW.DORSETTPRYCE.EXAMPLE
    </p>
  </section>

</main>
</body>
</html>
```